Specialist Doctor Personal Website

I wanted a website:
1. In my name
2. Describing my scope of practice
3. Having my photo
4. Has links to the places I work at
5. Provides patient information
6. Provides an email for contact

Target Market(s)

Victorian patients and GPs

Industry/Entity Type

Health

Coding

Coded - Design and coding required

Number of Pages Required

1 page

Font styles to use
Script

Colors
0054AA
0677BA
7BADD7
CADEEF
E8F1F8
6B429C
8869AF
B7A5CE
E3DAEB
F3F0F8

Requirements
Must have
• Modern design
Nice to have
• Links to email/fax/linkedin

```html
<!DOCTYPE html>
<html lang="en">
<head>
<meta charset="utf-8">
<title>AL — Specialist Doctor</title>
<link href="https://fonts.googleapis.com/css2?family=Marcellus&family=Roboto:wght@400;500;700&display=swap" rel="stylesheet">
<style>
:root{
  --blue:#0677BA;
  --blue-dark:#0054AA;
  --blue-mid:#7BADD7;
  --blue-light:#CADEEF;
  --blue-pale:#E8F1F8;
  --ink:#1b1b1b;
  --text:#555;
  --grey-bg:#f3f3f3;
  --contact-bg:#eef3fa;
  --footer:#1c1c1c;
  --white:#fff;
}
*{margin:0;padding:0;box-sizing:border-box}
html,body{width:1200px;height:4090px;overflow:hidden}
body{font-family:"Roboto",sans-serif;color:var(--text);background:var(--white);position:relative}
.serif{font-family:"Marcellus",serif}
section,header,footer{position:absolute;left:0;width:1200px}
.abs{position:absolute}
.btn{position:absolute;background:var(--blue);color:var(--white);font:700 13px "Roboto",sans-serif;display:flex;align-items:center;justify-content:center;text-transform:uppercase;border-radius:2px}
.heading{font-family:"Marcellus",serif;color:var(--ink);text-transform:uppercase;letter-spacing:1px}
.center-heading{position:absolute;left:0;width:1200px;text-align:center;font-size:44px}
.divider{position:absolute;left:536px;width:128px;height:16px}
.photo{position:absolute}

/* header */
.site-header{top:0;height:154px}
.logo{font-family:"Marcellus",serif;font-size:56px;color:var(--ink);left:111px;top:44px}
.call{left:873px;top:30px}
.call-icon{position:absolute;left:0;top:0;width:50px;height:50px;border-radius:50%;border:2px solid var(--blue-light)}
.call-label{position:absolute;left:46px;top:2px;font-size:11px;color:#777;white-space:nowrap;font-weight:500}
.call-number{position:absolute;left:46px;top:18px;font-size:20px;color:var(--blue);font-weight:700;white-space:nowrap}
.nav{position:absolute;top:115px;left:460px;display:flex;gap:0;font-size:13px;font-weight:500;color:var(--ink)}
.nav a{color:inherit;text-decoration:none;text-transform:uppercase;position:absolute;white-space:nowrap}
.nav-active{position:absolute;left:460px;top:96px;width:40px;height:3px;background:var(--blue)}

/* hero */
.hero{top:154px;height:600px;background:linear-gradient(90deg,#dbe9f3 0%,#eef4f8 35%,#f2ece2 60%,#e4ebf1 80%,#cbd9e6 100%)}
.hero-circle{left:37px;top:84px;width:158px;height:158px;border-radius:50%;background:rgba(123,173,215,.25)}
.hero-title{left:111px;top:156px;font-size:44px;line-height:50px}
.hero-text{left:111px;top:274px;width:420px;font-size:18px;line-height:29px;color:#444}
.dots{left:1134px;top:258px;width:14px}
.dot{width:12px;height:12px;border-radius:50%;background:var(--white);margin-bottom:11px}
.dot.on{background:var(--white);border:3px solid var(--blue)}

/* about */
.about{top:754px;height:711px}
.about-ring{left:111px;top:111px;width:482px;height:482px;border-radius:50%;background:radial-gradient(circle,#fff 60%,var(--blue-pale) 100%)}
.about-photo{left:164px;top:162px;width:376px;height:376px;border-radius:50%;background:linear-gradient(160deg,#d8dde3,#7d8ea6 55%,#24386a)}
.hi-pill{left:328px;top:511px;width:227px;height:51px;border-radius:26px;background:var(--white);box-shadow:0 4px 14px rgba(0,0,0,.12);display:flex;align-items:center;font-size:16px;color:var(--ink);font-weight:500}
.hi-pill span.ic{width:44px;height:44px;border-radius:50%;background:var(--blue);margin:0 28px 0 4px;display:flex;align-items:center;justify-content:center;border:3px solid var(--blue-light)}
.about-title{left:689px;top:154px;font-size:38px}
.about-line{left:689px;top:201px;width:120px;height:3px;background:var(--blue)}
.about-text{left:689px;top:240px;width:400px;font-size:13.5px;line-height:25.6px;text-align:justify}
.about-text p{margin-bottom:12px}

/* scope */
.scope{top:1465px;height:635px;background:var(--grey-bg)}
.card{position:absolute;top:178px;width:305px;height:380px;background:var(--white);box-shadow:0 3px 14px rgba(0,0,0,.1);border-radius:3px}
.card .photo{left:6px;top:6px;width:293px;height:216px}
.card h3{position:absolute;top:250px;width:100%;text-align:center;color:var(--blue);font-size:19px;font-weight:500}
.card p{position:absolute;top:290px;left:24px;right:24px;text-align:center;font-size:14px;line-height:25px}
.arrow-btn{position:absolute;width:34px;height:34px;border-radius:50%;display:flex;align-items:center;justify-content:center}

/* places */
.places{top:2100px;height:661px}
.places-band{left:0;top:0;width:1200px;height:447px;background:linear-gradient(180deg,var(--blue-dark),var(--blue) 70%,#0b6aad)}
.places-title{color:var(--white);top:60px}
.places-text{left:150px;width:900px;top:164px;text-align:center;color:var(--white);font-size:16px;line-height:27px}
.place{position:absolute;width:229px;height:277px;border:4px solid var(--white);box-shadow:0 4px 14px rgba(0,0,0,.2);border-radius:4px;overflow:hidden}
.place .photo{inset:0}
.place span{position:absolute;bottom:22px;width:100%;text-align:center;color:var(--white);font-weight:700;font-size:16px;text-transform:uppercase}

/* patient */
.patient{top:2761px;height:580px}
.patient-title{left:111px;top:40px;font-size:46px;line-height:51px}
.patient-line{left:111px;top:146px;width:87px;height:3px;background:var(--blue)}
.patient-text{left:111px;top:193px;width:470px;font-size:14px;line-height:25.6px;text-align:justify}
.patient-photo{left:660px;top:32px;width:428px;height:428px;border-radius:50%;border:9px solid var(--blue);background:linear-gradient(135deg,#a7b8c4,#6b8cae 50%,#385d8c)}

/* contact */
.contact{top:3341px;height:462px;background:var(--contact-bg)}
.field{position:absolute;background:var(--white);box-shadow:0 2px 6px rgba(0,0,0,.05);font-size:14px;color:#666;padding:15px 17px;border-radius:2px}

/* footer */
.site-footer{top:3803px;height:287px;background:var(--footer);color:var(--white)}
.f-logo{left:0;width:1200px;text-align:center;top:48px;font-family:"Marcellus",serif;font-size:56px}
.f-nav{left:0;width:1200px;top:130px;display:flex;justify-content:center;gap:36px;font-size:14px;font-weight:700;text-transform:uppercase}
.f-contact{left:0;width:1200px;top:165px;display:flex;justify-content:center;align-items:center;gap:18px;font-size:14px}
.f-line{left:111px;width:978px;top:213px;height:1px;background:#444}
.f-social{left:585px;top:198px;width:30px;height:30px;border-radius:50%;background:var(--blue)}
.f-copy{left:0;width:1200px;text-align:center;top:244px;font-size:12px;color:#ddd}
</style>
</head>
<body>

<header class="site-header">
  <div class="abs logo">AL</div>
  <div class="btn" style="left:624px;top:30px;width:187px;height:46px">Book Appointments</div>
  <div class="abs call">
    <div class="call-icon">
      <svg width="46" height="46" viewBox="0 0 46 46"><path d="M17 14c1-1 2-1 3 0l3 4c.6 1 .4 2-.4 2.7l-1.6 1.3c1 2.6 3 4.6 5.6 5.6l1.3-1.6c.7-.8 1.8-1 2.7-.4l4 3c1 1 1 2 0 3l-1.8 1.8c-1.5 1.5-4 1.7-6 .6-4.3-2.3-7.8-5.8-10.1-10.1-1.1-2-.9-4.5.6-6z" fill="none" stroke="#1b1b1b" stroke-width="1.8"/></svg>
    </div>
    <div class="call-label" style="left:46px;margin-left:14px">CLICK TO CALL:</div>
    <div class="call-number" style="margin-left:14px">+1 (555) 010 2030</div>
  </div>
  <div class="nav-active"></div>
  <nav class="nav" style="left:0;width:1200px">
    <a style="left:460px">Home</a>
    <a style="left:533px">About Me</a>
    <a style="left:635px">Services</a>
    <a style="left:732px">Patient Information</a>
    <a style="left:915px">Resources</a>
    <a style="left:1026px">Contact</a>
  </nav>
</header>

<section class="hero">
  <div class="photo" style="inset:0" role="img" aria-label="Blurred hospital corridor with a doctor in a white coat holding a stethoscope"></div>
  <div class="abs hero-circle"></div>
  <h1 class="abs heading hero-title" style="font-weight:400">Specialist<br>Doctor</h1>
  <p class="abs hero-text">Lorem ipsum dolor sit amet, consectetur adipis cing elit, sed do eiusmod tempor incididunt ut labore et dolore magna aliqua.</p>
  <div class="btn" style="left:111px;top:387px;width:189px;height:46px">Book Appointments</div>
  <div class="abs dots"><div class="dot"></div><div class="dot on"></div><div class="dot"></div><div class="dot"></div></div>
</section>

<section class="about">
  <div class="abs about-ring"></div>
  <div class="photo about-photo" role="img" aria-label="Portrait photo of the doctor in a navy blazer"></div>
  <div class="abs hi-pill"><span class="ic"><svg width="18" height="18" viewBox="0 0 18 18"><circle cx="9" cy="5.5" r="4" fill="#fff"/><path d="M1.5 17c0-4 3.4-6.5 7.5-6.5s7.5 2.5 7.5 6.5z" fill="#fff"/></svg></span>Hi I Am AL</div>
  <h2 class="abs heading about-title" style="font-weight:400">About Me</h2>
  <div class="abs about-line"></div>
  <div class="abs about-text">
    <p>Lorem ipsum dolor sit amet, consectetur adipiscing elit, sed do eiusmod tempor incididunt ut labore et dolore magna aliqua. Ut enim ad minim veniam, quis nostrud exercitation ullamco laboris nisi ut aliquip ex ea commodo consequat. Duis aute irure dolor in reprehenderit in voluptate.</p>
    <p>Lorem ipsum dolor sit amet, consectetur adipiscing elit, sed do eiusmod tempor incididunt ut labore et dolore magna aliqua. Ut enim ad minim veniam, quisea.</p>
  </div>
  <div class="btn" style="left:689px;top:492px;width:122px;height:46px">Read More</div>
</section>

<section class="scope">
  <h2 class="heading center-heading" style="top:68px;font-weight:400">My Scope of Practice</h2>
  <svg class="divider" style="top:120px" viewBox="0 0 128 16"><line x1="0" y1="8" x2="54" y2="8" stroke="#999"/><line x1="74" y1="8" x2="128" y2="8" stroke="#999"/><circle cx="64" cy="8" r="7" fill="none" stroke="#999"/><circle cx="64" cy="8" r="2.5" fill="var(--blue)"/></svg>
  <div class="card" style="left:111px"><div class="photo" style="background:linear-gradient(135deg,#d7dde2,#9aa6b1)" role="img" aria-label="Doctor shaking hands with a patient"></div><h3>LOREM IPSUM</h3><p>Lorem ipsum dolor sit amet, consecte tur adipiscing elit, sed do eiusmod tempor incididunt.</p></div>
  <div class="card" style="left:448px"><div class="photo" style="background:linear-gradient(135deg,#e3e6ea,#a9b4c0)" role="img" aria-label="Doctor writing notes on a clipboard"></div><h3>LOREM IPSUM</h3><p>Lorem ipsum dolor sit amet, consecte tur adipiscing elit, sed do eiusmod tempor incididunt.</p></div>
  <div class="card" style="left:784px"><div class="photo" style="background:linear-gradient(135deg,#e7e3df,#b6b3b0)" role="img" aria-label="Doctor showing a tablet to a patient"></div><h3>LOREM IPSUM</h3><p>Lorem ipsum dolor sit amet, consecte tur adipiscing elit, sed do eiusmod tempor incididunt.</p></div>
  <div class="arrow-btn" style="left:34px;top:350px;background:#fff;border:1px solid #bbb"><svg width="12" height="12" viewBox="0 0 12 12"><path d="M8 2L4 6l4 4" fill="none" stroke="#222" stroke-width="1.8"/></svg></div>
  <div class="arrow-btn" style="left:1131px;top:350px;background:var(--blue)"><svg width="12" height="12" viewBox="0 0 12 12"><path d="M4 2l4 4-4 4" fill="none" stroke="#fff" stroke-width="1.8"/></svg></div>
</section>

<section class="places">
  <div class="abs places-band" role="img" aria-label="Faint city skyline in blue tones"></div>
  <h2 class="heading center-heading places-title" style="font-weight:400">Places I Work</h2>
  <svg class="divider" style="top:120px" viewBox="0 0 128 16"><line x1="0" y1="8" x2="54" y2="8" stroke="#fff"/><line x1="74" y1="8" x2="128" y2="8" stroke="#fff"/><circle cx="64" cy="8" r="7" fill="none" stroke="#fff"/><circle cx="64" cy="8" r="2.5" fill="#fff"/></svg>
  <p class="abs places-text">Lorem ipsum dolor sit amet, consectetur adipiscing elit, sed do eiusmod tempor incididunt ut labore et dolore magna aliqua ut enim ad minim veniam, quis nostrud exercitation ullamco.</p>
  <div class="place" style="left:111px;top:308px"><div class="photo" style="background:linear-gradient(180deg,#9cc4e0,#2f7fae 55%,#1a4f78)" role="img" aria-label="Harbour with an opera house"></div><span>Lorem Ipsum</span></div>
  <div class="place" style="left:362px;top:273px"><div class="photo" style="background:linear-gradient(180deg,#5d86c2,#8a7f8a 55%,#c28a4a)" role="img" aria-label="City skyline at dusk over a river"></div><span>Lorem Ipsum</span></div>
  <div class="place" style="left:611px;top:308px"><div class="photo" style="background:linear-gradient(180deg,#7c8aa0,#c7a070 50%,#5a4b3a)" role="img" aria-label="City skyline at sunset with highways"></div><span>Lorem Ipsum</span></div>
  <div class="place" style="left:859px;top:273px"><div class="photo" style="background:linear-gradient(180deg,#4a86d0,#c59a5a 55%,#8a4a30)" role="img" aria-label="Historic bridge and city towers"></div><span>Lorem Ipsum</span></div>
  <svg class="abs" style="left:44px;top:360px" width="26" height="22" viewBox="0 0 26 22"><path d="M24 11H4M11 3L3 11l8 8" fill="none" stroke="#fff" stroke-width="3"/></svg>
  <svg class="abs" style="left:1128px;top:360px" width="26" height="22" viewBox="0 0 26 22"><path d="M2 11h20M15 3l8 8-8 8" fill="none" stroke="#fff" stroke-width="3"/></svg>
</section>

<section class="patient">
  <h2 class="abs heading patient-title" style="font-weight:400">Patient<br>Information</h2>
  <div class="abs patient-line"></div>
  <p class="abs patient-text">Lorem ipsum dolor sit amet, consectetur adipiscing elit, sed do eiusmod tempor incididunt ut labore et dolore magna aliqua. Ut enim ad minim veniam, quis nostrud exercitation ullamco laboris nisi ut aliquip ex ea commodo consequat duis aute irure dolor in repreh enderit in voluptate esse cillum dolorea. Lorem ipsum dolor sit amet, consectetur adipiscing elit, sed do eiusmod tempor incididunt ut labore et dolore magna aliqua.</p>
  <div class="btn" style="left:111px;top:400px;width:125px;height:46px">Read More</div>
  <div class="photo patient-photo" role="img" aria-label="Doctor in blue scrubs comforting an elderly patient"></div>
</section>

<section class="contact">
  <h2 class="heading center-heading" style="top:58px;font-weight:400">Contact Us</h2>
  <svg class="divider" style="top:117px" viewBox="0 0 128 16"><line x1="0" y1="8" x2="54" y2="8" stroke="#999"/><line x1="74" y1="8" x2="128" y2="8" stroke="#999"/><circle cx="64" cy="8" r="7" fill="none" stroke="#999"/><circle cx="64" cy="8" r="2.5" fill="var(--blue)"/></svg>
  <div class="field" style="left:165px;top:171px;width:283px;height:48px">Full Name</div>
  <div class="field" style="left:459px;top:171px;width:282px;height:48px">Phone Number</div>
  <div class="field" style="left:752px;top:171px;width:281px;height:48px">Email Address</div>
  <div class="field" style="left:165px;top:233px;width:868px;height:92px">Message...!</div>
  <div class="btn" style="left:519px;top:343px;width:162px;height:47px">Send Message</div>
</section>

<footer class="site-footer">
  <div class="abs f-logo">AL</div>
  <nav class="abs f-nav"><span>Home</span><span>About Me</span><span>Services</span><span>Patient Information</span><span>Resources</span><span>Contact</span></nav>
  <div class="abs f-contact">
    <span style="display:flex;align-items:center;gap:8px"><svg width="14" height="14" viewBox="0 0 14 14"><rect x="1" y="3" width="12" height="10" rx="1" fill="var(--blue)"/><rect x="4" y="1" width="6" height="3" fill="var(--blue)"/></svg>+1 (555) 010 2030</span>
    <span style="color:#888">|</span>
    <span style="display:flex;align-items:center;gap:8px"><svg width="16" height="12" viewBox="0 0 16 12"><rect width="16" height="12" rx="1" fill="var(--blue)"/><path d="M1 1l7 6 7-6" fill="none" stroke="#1c1c1c" stroke-width="1.3"/></svg>info@al-clinic.example</span>
  </div>
  <div class="abs f-line"></div>
  <div class="abs f-social" role="img" aria-label="Professional network link"></div>
  <div class="abs f-copy">© 2023 AL &nbsp;|&nbsp; All Rights Reserved</div>
</footer>

</body>
</html>
```